Website for Swedish wellness company "Heartmeadow"

We need a website for our Swedish wellness company. The name is "Heartmeadow" . The company is all about sustainablility for our body, soul and planet. We work with coaching, yoga, massage, healthy food, retreats(sports, excercise, sufing), healing and inspirational talks. We are convinced that personal sustainability and a strong spiritual connection to yourself will lead to planetary sustainability. Our customers are both companies and consumers from all over the world. The final design should be clean/simple and you should get a feeling of community, happiness, warmth, connection,, joy, spirituality but still a professional touch.Just got a logo from Pixel Harbor and are very happy with it;-)
Updates

Sorry I was too enthusiastic posting this project. Of course I will give you some text as well för the different pages! I will see to that it is finished by friday so if you want to wait with your submissions please do! Best regards Maria

Target Market(s)

Businesses and consumers

Industry/Entity Type

Health And Wellness

Number of Pages Required

5+ page

Font styles to use
Sans Serif

Colors
33a6d7
00a990
b7a5cd

Requirements
Must have
• Idea about pages:
• I am not sure how many pages I get for the price, but 5 would be nice to start with.
• Not sure what write ups is;-)
• But title of the pages could be:
• Landing page
• About us
• Services
• Retreats
• Contact us
Nice to have
• A clean and professional website but with some heart and soul in it. Because we Would love colours that harmonize with our logo, but other ideas are welcome!

```html
<!DOCTYPE html>
<html lang="en">
<head>
<meta charset="utf-8">
<title>Heartmeadow – Wellness</title>
<link href="https://fonts.googleapis.com/css2?family=Roboto:wght@400;500;700&display=swap" rel="stylesheet">
<style>
:root{
  --teal:#5cc7c8;
  --teal-dark:#4f9c9c;
  --navy:#0d3a6b;
  --navy-deep:#0b3770;
  --text:#4a4f57;
  --grey-soft:#e3e7ee;
  --white:#ffffff;
  --star:#f2a33a;
}
*{box-sizing:border-box;margin:0;padding:0}
html,body{width:1200px;height:3509px;overflow:hidden}
body{position:relative;font-family:'Roboto',sans-serif;color:var(--text);background:var(--white)}
.abs{position:absolute}
a{text-decoration:none;color:inherit}

/* header */
.brand{left:88px;top:14px;display:flex;align-items:center;gap:10px;font-size:22px;font-weight:500;color:var(--navy);letter-spacing:.5px}
.brand-dot{width:38px;height:38px;border-radius:50%;border:3px solid var(--teal)}
.nav{right:88px;top:27px;display:flex;gap:30px;font-size:13px;font-weight:500;color:var(--navy)}
.nav .active{color:var(--teal)}

/* hero */
.hero-kicker{left:88px;top:278px;font-size:42px;font-weight:500;color:var(--teal)}
.hero-title{left:86px;top:318px;font-size:66px;font-weight:700;color:var(--navy);letter-spacing:-.5px}
.hero-text{left:88px;top:398px;width:370px;font-size:14.5px;line-height:23px}
.btn{left:88px;top:459px;width:194px;height:38px;border-radius:19px;background:var(--navy);color:var(--white);font-size:13px;font-weight:700;display:flex;align-items:center;justify-content:center;gap:8px}
.hero-ring{left:562px;top:105px;width:548px;height:548px;border-radius:50%;border:15px solid var(--teal);overflow:hidden}
.hero-photo{width:100%;height:100%;background:linear-gradient(180deg,#9fc8e4 0%,#c9dfe9 45%,#8fb0c2 70%,#b9c7ce 100%)}
.slider-dots{left:1146px;top:360px;display:flex;flex-direction:column;align-items:flex-end;gap:8px;font-size:10px;color:var(--teal)}
.slider-dots span{display:flex;align-items:center;gap:5px}
.slider-dots i{display:block;width:9px;height:9px;border-radius:50%;border:1.5px solid #b7bcc4}
.slider-dots .on i{border-color:var(--teal);width:10px;height:10px}
.scroll-down{left:580px;top:650px;width:40px;height:40px;border-radius:50%;border:2px solid var(--teal)}

/* mission */
.mission-bg{left:-41px;top:647px;width:340px;height:340px;border-radius:50%;background:var(--grey-soft)}
.mission-photo{left:88px;top:772px;width:444px;height:444px;border-radius:50%;background:radial-gradient(circle at 50% 40%,#c8b6a8 0%,#a7c9cb 45%,#d9d4d2 100%)}
.section-icon{width:32px;height:32px;border-radius:50%;border:2px solid var(--teal)}
.mission-head{left:601px;top:763px;display:flex;align-items:center;gap:12px}
.mission-head h2{font-size:41px;font-weight:700;color:var(--navy)}
.mission-body{left:605px;top:826px;width:508px;font-size:14.5px;line-height:23px}
.mission-body p{margin-bottom:12px}

/* services */
.services-wave{left:0;top:1240px}
.services-head{left:0;top:1414px;width:1200px;text-align:center;color:var(--white)}
.services-head .section-icon{border-color:var(--white);margin:0 auto 8px}
.services-head h2{font-size:42px;font-weight:700}
.services-head p{width:760px;margin:10px auto 0;font-size:14.5px;line-height:21px}
.service{top:1597px;width:160px;text-align:center;color:var(--white);font-size:18px;font-weight:500;line-height:20px}
.service .disc{width:132px;height:132px;border-radius:50%;background:var(--white);margin:0 auto 14px;display:flex;align-items:center;justify-content:center}
.service .disc.dark{background:var(--navy)}

/* news */
.news-head{left:0;top:1992px;width:1200px;text-align:center}
.news-head .section-icon{margin:0 auto 4px}
.news-head h2{font-size:43px;font-weight:700;color:var(--navy)}
.news-photo{top:2093px;width:320px;height:227px}
.news-card{top:2272px;width:298px;height:180px;background:var(--white);box-shadow:0 6px 24px rgba(13,58,107,.12);padding:30px 32px}
.news-card h3{font-size:16px;font-weight:500;color:var(--navy);line-height:19px}
.news-card p{font-size:13px;line-height:18px;margin-top:6px}
.news-card a{display:block;margin-top:10px;font-size:12px;font-weight:700;color:var(--navy)}
.news-date{top:2217px;width:54px;height:55px;background:var(--teal);color:var(--white);text-align:center;padding-top:7px}
.news-date b{display:block;font-size:22px;line-height:22px}
.news-date small{font-size:10px;font-weight:700}

/* testimonial */
.client-bg{left:0;top:2480px;width:1200px;height:600px;background:linear-gradient(180deg,#fff 0%,#eef3f8 100%)}
.client-photo{left:735px;top:2506px;width:465px;height:640px;border-radius:200px 0 0 0;background:linear-gradient(180deg,#c69a7e 0%,#e9ecef 40%,#f4f6f8 100%)}
.client-head{left:300px;top:2586px;width:600px;text-align:center}
.client-head .section-icon{margin:0 auto 6px}
.client-head h2{font-size:43px;font-weight:700;color:var(--navy)}
.quote-mark{left:556px;top:2650px;font-size:160px;font-weight:700;color:#d6d9de;line-height:1}
.client-text{left:300px;top:2734px;width:600px;text-align:center;font-size:18.5px;line-height:27px;color:#3d434c}
.stars{left:0;top:2818px;width:1200px;text-align:center;color:var(--star);font-size:20px;letter-spacing:4px}
.client-name{left:0;top:2851px;width:1200px;text-align:center;color:var(--teal);font-size:16px;font-weight:500}
.client-dots{left:581px;top:2886px;display:flex;gap:6px}
.client-dots i{width:8px;height:8px;border-radius:50%;background:#c5c9cf}
.client-dots i.on{background:var(--teal)}

/* footer */
.footer-wave{left:0;top:3000px}
.foot-brand{left:68px;top:3215px;width:232px;text-align:center;color:var(--white)}
.foot-brand .brand-dot{width:86px;height:86px;border-width:4px;margin:0 auto 12px}
.foot-brand span{font-size:28px;font-weight:500;letter-spacing:1px}
.foot-col{top:3218px;color:var(--white);font-size:13px}
.foot-col h4{color:var(--teal);font-size:16px;font-weight:500;margin-bottom:14px}
.foot-col li{list-style:none;margin:0 0 14px 2px}
.subscribe{width:230px;height:37px;background:#1e4c82;margin-top:14px;display:flex;align-items:center;justify-content:space-between;padding:0 14px 0 18px;font-size:12px}
.contact-line{display:flex;align-items:center;gap:6px;margin-bottom:6px}
.contact-sub{color:var(--teal);margin:-2px 0 10px 0}
.view-detail{color:var(--teal);font-size:11px;font-weight:500;text-decoration:underline;margin-top:12px;display:block}
.foot-rule{left:88px;top:3459px;width:1024px;height:1px;background:#2a5a8f}
.to-top{left:1114px;top:3440px;width:38px;height:38px;border-radius:50%;background:var(--teal);display:flex;align-items:center;justify-content:center}
.copyright{left:0;top:3480px;width:1200px;text-align:center;color:var(--white);font-size:12px}
</style>
</head>
<body>

<!-- header -->
<div class="abs brand"><span class="brand-dot"></span>HEARTMEADOW</div>
<nav class="abs nav"><a class="active">HOME</a><a>ABOUT US</a><a>SERVICES</a><a>RETREATS</a><a>CONTACT US</a></nav>

<!-- hero -->
<div class="abs hero-kicker">Welcome to</div>
<h1 class="abs hero-title">Heartmeadow</h1>
<p class="abs hero-text">Lorem Ipsum is simply dummy text of the printing and typesetting industry lorem Ipsum has been .</p>
<a class="abs btn">Make An Appointment
<svg width="14" height="10" viewBox="0 0 14 10"><path d="M1 5h11M8 1l4 4-4 4" fill="none" stroke="#fff" stroke-width="1.5"/></svg></a>
<div class="abs hero-ring"><div class="hero-photo" role="img" aria-label="Woman doing a handstand on a beach"></div></div>
<div class="abs slider-dots">
  <span class="on">01 <i></i></span><span><i></i></span><span><i></i></span><span><i></i></span>
</div>
<div class="abs scroll-down">
  <svg width="36" height="36" viewBox="0 0 36 36"><path d="M14 16l4 4 4-4" fill="none" stroke="#5cc7c8" stroke-width="1.5"/></svg>
</div>

<!-- mission -->
<div class="abs mission-bg"></div>
<div class="abs mission-photo" role="img" aria-label="Woman stretching forward on a yoga mat"></div>
<div class="abs mission-head"><span class="section-icon"></span><h2>Heartmeadow´s mission</h2></div>
<div class="abs mission-body">
  <p>Heartmeadow´s mission is to bring people and organisations back to an optimal state of health. Sustainability for the body, soul and planet is our ultimate goal. There are several roads there depending on what suits you as an individual or as an organisation. We work with mental training (training the mind), yoga, massage, energy medicine and personal guidance/coaching on different levels for a true state of well-being, that is sustained over time.</p>
  <p>We are convinced that a sustainable state of health is only achieved if you approach it from a holistic point of view. We need to come back to balance not only in mind and body, but also emotionally and spiritually.<br>If we reach balance in ourselves and have the tools to sustain it, we will be able to make conscious decisions in our lives and then we will start to thrive and can reach our full potential- our authentic selfs.</p>
  <p>At Heartmeadow we believe that authenticity is key for both individuals and organisations. When you are aligned with your core values the customers or the people around you will feel it – and support you.</p>
</div>

<!-- services -->
<svg class="abs services-wave" width="1200" height="740" viewBox="0 1240 1200 740" role="img" aria-label="Services band over a soft massage photo">
  <defs><linearGradient id="svcFill" x1="0" y1="0" x2="1" y2="1"><stop offset="0" stop-color="#4a9596"/><stop offset="1" stop-color="#55a4a3"/></linearGradient></defs>
  <path d="M0 1273 C120 1245 240 1238 380 1252 C620 1280 840 1385 1200 1368 L1200 1961 C900 1950 620 1860 400 1832 C240 1812 120 1818 0 1846 Z" fill="url(#svcFill)"/>
  <g fill="none" stroke="#fff" stroke-width="2">
    <circle cx="437" cy="1663" r="66"/><circle cx="598" cy="1663" r="66"/><circle cx="761" cy="1663" r="66"/>
  </g>
</svg>
<div class="abs services-head">
  <span class="section-icon"></span>
  <h2>Our Services</h2>
  <p>We are passionate about assisting you in creating a sustainable, healthy life where you can reach your full potential. Also a company is only as healthy and prosperous as its employees. We can supply th assistance, coaching and the tools you need to excel and take giant steps toward a sustainable and enjoyable future.</p>
</div>
<div class="abs service" style="left:278px">
  <div class="disc"><svg width="54" height="54" viewBox="0 0 54 54"><circle cx="27" cy="18" r="10" fill="#0d3a6b"/><path d="M9 46c0-11 8-16 18-16s18 5 18 16z" fill="#0d3a6b"/></svg></div>Workshops</div>
<div class="abs service" style="left:436px">
  <div class="disc dark"><svg width="54" height="54" viewBox="0 0 54 54"><circle cx="27" cy="11" r="6" fill="#fff"/><path d="M17 20h20v6H17z" fill="#fff"/><path d="M19 28h16l-3 20H22z" fill="#fff"/></svg></div>Inspirational<br>lectures</div>
<div class="abs service" style="left:600px">
  <div class="disc"><svg width="54" height="54" viewBox="0 0 54 54"><circle cx="27" cy="11" r="6" fill="#0d3a6b"/><path d="M21 20h12l2 16h-16z" fill="#0d3a6b"/><path d="M9 44c6-6 12-8 18-8s12 2 18 8z" fill="#0d3a6b"/></svg></div>Retreats</div>
<div class="abs service" style="left:762px">
  <div class="disc"><svg width="60" height="54" viewBox="0 0 60 54"><circle cx="42" cy="9" r="5" fill="#0d3a6b"/><path d="M32 10l10 10 10-10M39 20h6v26h-6z" fill="#0d3a6b" stroke="#0d3a6b" stroke-width="3"/><circle cx="18" cy="24" r="5" fill="#0d3a6b"/><path d="M8 44l10-14 10 14z" fill="#0d3a6b"/></svg></div>Individual<br>coaching</div>

<!-- news -->
<div class="abs news-head"><span class="section-icon"></span><h2>Latest News</h2></div>

<div class="abs news-photo" style="left:101px;background:linear-gradient(135deg,#eef0ee,#d8b9a3 55%,#9bb36a)" role="img" aria-label="Woman holding a bag of fresh vegetables"></div>
<div class="abs news-date" style="left:112px"><b>05</b><small>AUG</small></div>
<div class="abs news-card" style="left:112px"><h3>Lorem Ipsum is simply dummy text of the printing ..</h3><p>Lorem Ipsum is simply dummy text of the printing and typesetting industry. Lorem Ipsum has been.</p><a>READ MORE</a></div>

<div class="abs news-photo" style="left:437px;background:linear-gradient(135deg,#c9c3b1,#8d9aa3 50%,#c79a5e)" role="img" aria-label="Two people doing yoga in a studio"></div>
<div class="abs news-date" style="left:448px"><b>05</b><small>AUG</small></div>
<div class="abs news-card" style="left:448px"><h3>Lorem Ipsum is simply dummy text of the printing ..</h3><p>Lorem Ipsum is simply dummy text of the printing and typesetting industry. Lorem Ipsum has been.</p><a>READ MORE</a></div>

<div class="abs news-photo" style="left:774px;background:linear-gradient(135deg,#6d5a4c,#d7a988 50%,#f1ede9)" role="img" aria-label="Man receiving a relaxing face massage"></div>
<div class="abs news-date" style="left:785px"><b>05</b><small>AUG</small></div>
<div class="abs news-card" style="left:785px"><h3>Lorem Ipsum is simply dummy text of the printing ..</h3><p>Lorem Ipsum is simply dummy text of the printing and typesetting industry. Lorem Ipsum has been.</p><a>READ MORE</a></div>

<!-- testimonial -->
<div class="abs client-bg"></div>
<div class="abs client-photo" role="img" aria-label="Woman meditating in a white shirt"></div>
<div class="abs client-head"><span class="section-icon"></span><h2>What Client Says</h2></div>
<div class="abs quote-mark">“</div>
<p class="abs client-text">Lorem Ipsum is simply dummy text of the printing and typesetting industry. Lorem Ipsum has been the industry's standard dummy text ever since the 1500s, when an unknown printer .</p>
<div class="abs stars">★★★★★</div>
<div class="abs client-name">Anna Berg</div>
<div class="abs client-dots"><i class="on"></i><i></i><i></i></div>

<!-- footer -->
<svg class="abs footer-wave" width="1200" height="509" viewBox="0 3000 1200 509" aria-hidden="true">
  <path d="M0 3022 C200 3000 420 3010 620 3060 C820 3110 1000 3160 1200 3140 L1200 3509 L0 3509 Z" fill="#0b3770"/>
</svg>
<div class="abs foot-brand"><div class="brand-dot"></div><span>HEARTMEADOW</span></div>
<div class="abs foot-col" style="left:383px">
  <h4>USEFUL LINKS</h4>
  <ul><li>Home</li><li>About us</li><li>Services</li><li>Retreats</li><li>Contact us</li></ul>
</div>
<div class="abs foot-col" style="left:569px">
  <h4>NEWSLETTER</h4>
  <div>Subscribe to our newsletter</div>
  <div class="subscribe"><span>Email Address</span>
    <svg width="14" height="14" viewBox="0 0 14 14"><path d="M1 7l12-6-4 12-2-5z" fill="#5cc7c8"/></svg></div>
</div>
<div class="abs foot-col" style="left:862px">
  <h4>CONTACT US</h4>
  <div class="contact-line"><svg width="9" height="12" viewBox="0 0 9 12"><path d="M4.5 0a4.5 4.5 0 0 1 4.5 4.5C9 8 4.5 12 4.5 12S0 8 0 4.5A4.5 4.5 0 0 1 4.5 0z" fill="#5cc7c8"/><circle cx="4.5" cy="4.5" r="1.6" fill="#0b3770"/></svg>Ängsvägen 12, 512 34 Lindby SWEDEN</div>
  <div class="contact-sub">Erik Lindqvist</div>
  <div class="contact-line"><svg width="11" height="11" viewBox="0 0 11 11"><path d="M2 0l2 3-1 1.5c.7 1.5 2 2.8 3.5 3.5L8 7l3 2-1 2C5 11 0 6 0 1z" fill="#5cc7c8"/></svg>0046701 234567</div>
  <div class="contact-line"><svg width="12" height="9" viewBox="0 0 12 9"><rect width="12" height="9" fill="#5cc7c8"/><path d="M0 0l6 5 6-5" fill="none" stroke="#0b3770"/></svg>erik@heartmeadow.se</div>
  <a class="view-detail">VIEW DETAIL</a>
</div>
<div class="abs foot-rule"></div>
<div class="abs to-top"><svg width="12" height="8" viewBox="0 0 12 8"><path d="M2 6l4-4 4 4" fill="none" stroke="#fff" stroke-width="1.5"/></svg></div>
<div class="abs copyright">Copyright 2019 | All Right Reserved</div>

</body>
</html>
```